Lumara Health & Wellness Business Card Design

We would like to create business cards matching with our new logo design. The card should be professional looking but still have a playful side and something that would be eye catching. We are planing to open a luxury medical spa and looking to create a design based on this new logo. We are looking for a design that shows off luxury but not be gold in color. Also, while we are a more female oriented medical center we do have men that come in for our services and it should be be too feminine.

Target Market(s)

Health & Wellness. Medical patients. Luxury spa

Industry/Entity Type

Health And Wellness

Contact Information for Business Card

It should have the logo design in the front of card and back of card should have our contact information. Our current colors are peach/ coral, teal, and gray. We are looking for a modern looking design.

Font styles to use
Script

Colors
32a6d6
e667a6
86cfc6
fece3e

Requirements
Must have
• It should have our logo design. We would prefer to have a more modern look to the card.
Nice to have
• Eye-Catching Design on the personable side but still classy.
Should not have
• At this point we are looking for the best design. It should not have color purple.

```html
<!DOCTYPE html>
<html lang="en">
<head>
<meta charset="utf-8">
<title>Lumara Health & Wellness – Business Card</title>
<link href="https://fonts.googleapis.com/css2?family=Arimo:wght@400&family=Pinyon+Script&display=swap" rel="stylesheet">
<style>
  :root {
    --backdrop: #747478;
    --card: #e6e7e9;
    --coral: #ff7a70;
    --teal: #008f82;
    --ink: #000000;
    --line: #f4a59d;
    --blush: rgba(244, 165, 157, 0.22);
  }
  * { margin: 0; padding: 0; box-sizing: border-box; }
  html, body { width: 1200px; height: 1200px; overflow: hidden; }
  body {
    background: var(--backdrop);
    position: relative;
    font-family: "Arimo", Arial, sans-serif;
    color: var(--ink);
  }
  .card {
    position: absolute;
    left: 168px;
    width: 864px;
    height: 488px;
    background: var(--card);
    overflow: hidden;
  }
  .card--contact { top: 64px; }
  .card--brand { top: 618px; }

  .card__pattern {
    position: absolute;
    inset: 0;
    background:
      linear-gradient(120deg, var(--blush) 0%, rgba(230, 231, 233, 0) 38%),
      linear-gradient(300deg, var(--blush) 0%, rgba(230, 231, 233, 0) 38%),
      var(--card);
  }

  .card__bands { position: absolute; inset: 0; width: 100%; height: 100%; }
  .band--coral { fill: var(--coral); }
  .band--teal { fill: var(--teal); }
  .band--black { fill: var(--ink); }

  .holder {
    position: absolute;
    left: 0; right: 0;
    top: 52px;
    text-align: center;
    padding-left: 64px;
  }
  .holder__name {
    font-family: "Pinyon Script", cursive;
    font-size: 44px;
    font-weight: 400;
    letter-spacing: 0.32em;
    line-height: 1;
  }
  .holder__business {
    margin-top: 14px;
    font-size: 12px;
    letter-spacing: 0.45em;
  }
  .holder__rule {
    position: absolute;
    left: 322px;
    top: 133px;
    width: 280px;
    height: 2px;
    background: var(--line);
  }

  .contact-list { list-style: none; }
  .contact-item {
    position: absolute;
    left: 292px;
    display: flex;
    align-items: center;
    height: 44px;
  }
  .contact-item__icon {
    width: 44px; height: 44px;
    border-radius: 50%;
    background: var(--ink);
    display: flex; align-items: center; justify-content: center;
    flex: none;
  }
  .contact-item__icon svg { width: 20px; height: 20px; fill: none; stroke: #fff; stroke-width: 2; }
  .contact-item__icon svg .solid { fill: #fff; stroke: none; }
  .contact-item__text {
    margin-left: 37px;
    font-size: 14.5px;
    line-height: 1.28;
    white-space: nowrap;
  }

  .brand-name {
    position: absolute;
    left: 0; right: 0;
    top: 176px;
    text-align: center;
    font-weight: 400;
    color: var(--ink);
  }
  .brand-name__word { display: block; font-size: 78px; letter-spacing: 0.12em; line-height: 1; }
  .brand-name__tagline { display: block; margin-top: 14px; font-size: 26px; letter-spacing: 0.08em; }
</style>
</head>
<body>

<section class="card card--contact" aria-label="Business card, contact side">
  <div class="card__pattern" role="img" aria-label="Soft coral geometric line pattern across the card background"></div>
  <svg class="card__bands" viewBox="0 0 1080 608" preserveAspectRatio="none" aria-hidden="true">
    <rect class="band--coral" x="80" y="0" width="452" height="25"/>
    <rect class="band--teal" x="532" y="0" width="491" height="38"/>
    <rect class="band--black" x="1023" y="0" width="57" height="38"/>
    <rect class="band--black" x="0" y="571" width="56" height="37"/>
    <rect class="band--teal" x="56" y="571" width="491" height="37"/>
    <rect class="band--coral" x="547" y="582" width="433" height="26"/>
  </svg>

  <header class="holder">
    <h1 class="holder__name">Nora Vale</h1>
    <p class="holder__business">BUSINESS NAME</p>
  </header>
  <div class="holder__rule"></div>

  <ul class="contact-list">
    <li class="contact-item" style="top:165px">
      <span class="contact-item__icon">
        <svg viewBox="0 0 24 24"><path class="solid" d="M12 2a7 7 0 0 0-7 7c0 5 7 13 7 13s7-8 7-13a7 7 0 0 0-7-7zm0 9.5a2.5 2.5 0 1 1 0-5 2.5 2.5 0 0 1 0 5z"/></svg>
      </span>
      <span class="contact-item__text">YOUR FIRST ADDRESS LINE<br>YOUR SECOND ADDRESS LINE</span>
    </li>
    <li class="contact-item" style="top:229px">
      <span class="contact-item__icon">
        <svg viewBox="0 0 24 24"><rect x="3" y="6" width="18" height="12"/><polyline points="3,6 12,13 21,6"/><polyline points="3,18 10,11.5"/><polyline points="21,18 14,11.5"/></svg>
      </span>
      <span class="contact-item__text">NORA.VALE@YOURMAIL.COM</span>
    </li>
    <li class="contact-item" style="top:293px">
      <span class="contact-item__icon">
        <svg viewBox="0 0 24 24"><path class="solid" d="M6.6 10.8a15.2 15.2 0 0 0 6.6 6.6l2.2-2.2a1 1 0 0 1 1-.25 11.4 11.4 0 0 0 3.6.57 1 1 0 0 1 1 1V20a1 1 0 0 1-1 1A17 17 0 0 1 3 4a1 1 0 0 1 1-1h3.5a1 1 0 0 1 1 1 11.4 11.4 0 0 0 .57 3.6 1 1 0 0 1-.25 1z"/></svg>
      </span>
      <span class="contact-item__text">+0 123 456 789<br>+0 987 654 321</span>
    </li>
    <li class="contact-item" style="top:357px">
      <span class="contact-item__icon">
        <svg viewBox="0 0 24 24"><circle cx="12" cy="12" r="9"/><ellipse cx="12" cy="12" rx="4" ry="9"/><line x1="3" y1="12" x2="21" y2="12"/><line x1="4.5" y1="7.5" x2="19.5" y2="7.5"/><line x1="4.5" y1="16.5" x2="19.5" y2="16.5"/></svg>
      </span>
      <span class="contact-item__text">WWW.YOURCOMPANY.COM</span>
    </li>
  </ul>
</section>

<section class="card card--brand" aria-label="Business card, brand side">
  <div class="card__pattern" role="img" aria-label="Soft coral geometric line pattern across the card background"></div>
  <svg class="card__bands" viewBox="0 0 1080 608" preserveAspectRatio="none" aria-hidden="true">
    <rect class="band--coral" x="0" y="0" width="385" height="25"/>
    <rect class="band--teal" x="385" y="0" width="430" height="37"/>
    <rect class="band--black" x="815" y="0" width="57" height="37"/>
    <rect class="band--black" x="206" y="572" width="56" height="36"/>
    <rect class="band--teal" x="262" y="572" width="430" height="36"/>
    <rect class="band--coral" x="692" y="583" width="388" height="25"/>
  </svg>

  <h2 class="brand-name">
    <span class="brand-name__word">LUMARA</span>
    <span class="brand-name__tagline">HEALTH &amp; WELLNESS</span>
  </h2>
</section>

</body>
</html>
```